Consulting/Brand Licensing business needs business card

We need a business card created for our IP company, that also does consulting and brand licensing. We would like this card to be vague, as our other business' are in the cannabis industry and this is a non-cannabis touching entity. Perhaps something that hints vaguely at the industry without alerting or possibly offending the receiver.

Target Market(s)

CEOs/Key Decision Makers/Industry Leaders

Contact Information for Business Card

No address, simply list Seattle, WA. Phone: 206-555-0147. Name: Dilan Vesterby // email: Dilan@pulvanixa.com

Colors

Designer to choose colors to be used in the design.

Requirements
Must have
• Logo, Name, Email, Phone number, "Consulting, Licensing and Branding Specialists"
Nice to have
• We would like this to be more professional than playful.

```html
<!DOCTYPE html>
<html lang="en">
<head>
<meta charset="utf-8">
<title>Pulvanixa, Inc — Business Card</title>
<link rel="stylesheet" href="https://fonts.googleapis.com/css2?family=Questrial&family=Montserrat:wght@600;700&display=swap">
<style>
  :root {
    --page: #e9e7e4;
    --card-dark: #1e1e1e;
    --paper: #ffffff;
    --accent: #e04e2b;
    --divider: #151515;
    --ink: #1c1c1c;
    --light-text: #ffffff;
  }
  * { box-sizing: border-box; margin: 0; padding: 0; }
  html, body { width: 1200px; height: 960px; overflow: hidden; }
  body {
    background: var(--page);
    display: flex;
    flex-direction: column;
    align-items: center;
    justify-content: center;
    gap: 64px;
    font-family: "Questrial", sans-serif;
  }
  .card {
    width: 600px;
    height: 343px;
    position: relative;
    overflow: hidden;
    box-shadow: 0 6px 18px rgba(0,0,0,0.18);
  }
  .brand-name {
    font-family: "Montserrat", sans-serif;
    font-weight: 700;
    color: var(--accent);
    letter-spacing: 1px;
    line-height: 1;
  }
  .brand-legal {
    font-size: 22px;
    line-height: 1;
    margin-top: 16px;
  }

  /* Front */
  .card-front {
    background: var(--card-dark);
    display: flex;
    flex-direction: column;
    align-items: center;
    justify-content: center;
    text-align: center;
  }
  .card-front .brand-name { font-size: 60px; }
  .card-front .brand-legal { color: var(--light-text); }
  .tagline {
    color: var(--light-text);
    font-size: 14px;
    letter-spacing: 0.5px;
    margin-top: 14px;
    opacity: 0.85;
  }

  /* Back */
  .card-back { background: var(--paper); }
  .card-back .brand-block {
    position: absolute;
    left: 0;
    top: 0;
    width: 58%;
    height: 100%;
    display: flex;
    flex-direction: column;
    align-items: center;
    justify-content: center;
    padding-right: 24px;
    padding-top: 20px;
  }
  .card-back .brand-name { font-size: 46px; }
  .card-back .brand-legal { color: var(--ink); }

  .divider-line,
  .contact-panel {
    position: absolute;
    inset: 0;
  }
  .divider-line {
    background: var(--divider);
    clip-path: polygon(62.5% 0, 100% 0, 100% 100%, 56.5% 100%);
  }
  .contact-panel {
    background: var(--accent);
    clip-path: polygon(63.3% 0, 100% 0, 100% 100%, 57.3% 100%);
  }
  .contact {
    position: absolute;
    right: 26px;
    top: 78px;
    text-align: right;
    color: var(--light-text);
  }
  .contact-name {
    font-family: "Montserrat", sans-serif;
    font-weight: 600;
    font-size: 18px;
  }
  .contact-role {
    font-size: 15px;
    margin-top: 4px;
  }
  .contact-lines {
    list-style: none;
    margin-top: 24px;
    font-size: 15px;
    line-height: 1.55;
  }
  .contact-lines li {
    display: flex;
    align-items: center;
    justify-content: flex-end;
    gap: 7px;
  }
  .contact-lines svg { width: 13px; height: 13px; flex: none; }
</style>
</head>
<body>

  <section class="card card-front" aria-label="Card front">
    <span class="brand-name">Pulvanixa</span>
    <p class="brand-legal">Pulvanixa, Inc</p>
    <p class="tagline">Consulting, Licensing and Branding Specialists</p>
  </section>

  <section class="card card-back" aria-label="Card back">
    <div class="brand-block">
      <span class="brand-name">Pulvanixa</span>
      <p class="brand-legal">Pulvanixa, Inc</p>
    </div>
    <div class="divider-line"></div>
    <div class="contact-panel"></div>
    <div class="contact">
      <p class="contact-name">Dilan Vesterby</p>
      <p class="contact-role">President</p>
      <ul class="contact-lines">
        <li>
          <svg viewBox="0 0 16 16" aria-hidden="true">
            <circle cx="8" cy="8" r="7" fill="none" stroke="#fff" stroke-width="1.4"/>
            <path d="M5.6 4.6l1.2 1.6-.7.9c.5 1.1 1.3 1.9 2.4 2.4l.9-.7 1.6 1.2-.6 1.2c-2.8-.3-5-2.5-5.3-5.3z" fill="#fff"/>
          </svg>
          <span>206-555-0147</span>
        </li>
        <li>
          <svg viewBox="0 0 16 16" aria-hidden="true">
            <rect x="1.5" y="5" width="13" height="9" fill="#fff"/>
            <path d="M1.5 5L8 1.5 14.5 5 8 9.5z" fill="none" stroke="#fff" stroke-width="1.2"/>
            <path d="M1.5 5L8 10l6.5-5" fill="none" stroke="#e04e2b" stroke-width="1.2"/>
          </svg>
          <span>Dilan@pulvanixa.com</span>
        </li>
        <li>
          <svg viewBox="0 0 16 16" aria-hidden="true">
            <path d="M8 1.2a4.6 4.6 0 0 0-4.6 4.6C3.4 9.3 8 14.8 8 14.8s4.6-5.5 4.6-9A4.6 4.6 0 0 0 8 1.2z" fill="#fff"/>
            <circle cx="8" cy="5.8" r="1.7" fill="#e04e2b"/>
          </svg>
          <span>Seattle, WA</span>
        </li>
      </ul>
    </div>
  </section>

</body>
</html>
```